Young judge needs a website to publish and to connect

I would like to have a website where I can publish my articles in public law. I am judge at the Alpine Civic Review Tribunal. Therefore, the website must have a calm, friendly and fairly neutral design. Also, it should be mobile friendly and easy to use.

On my website, I want to

- publish articles such as https://www.brindlepost.example/pulse/how-win-court-tobias-wenger/ and get feedbacks from my colleagues
- generate interest for my project on 'Statutes and Society - Notes from the Chamber', a book that I would like to publish in 2020 and which brings together my publications on public law (http://www.civicnorm.example/content/english/profil/publikationen.html ).
- provide updates for my university courses on constitutional, administrative and international law.

For that purpose, I would kindly ask you to suggest a website that communicates a fresh approach to the work of a young judge in constitutional and administrative law. Please have in mind that I do not only sit on the bench, but that I also work in academia. Therefore, it should be suitable for an audience from both university and law practice. The website should replace the existing website on www.civicnorm.example that I designed when still working as a lawyer. Thank you.

Target Market(s)

Academica, law firms, courts

Industry/Entity Type

University

Contact Information for Business Card

Tobias Wenger
Judge
Alpine Civic Review Tribunal
M +41 79 5XX 8X 2X

Logo Text

Notes from the Chamber

Number of Pages Required

5+ page

Font styles to use
Sans Serif

Colors
0455a3

Requirements
Must have
• - a page where I can publish and get feedbacks
• - a page about my project on law and politics
• - a page where I can provide updates for my university courses on constitutional, administrative and international law
• - page where I can list current and planned projects
• - a collaborative, young and fresh approach
Nice to have
• - a page reserved for my colleagues at the Alpine Civic Review Tribunal where I can alert them about to possibility to collaborate (if possibly password protected) and where they may suggest what to contribute to a specific project
Should not have
• anything which might to suggest that I want to make money with it, bragging or pretentious. Do not forget: I am judge, not a barrister.

```html
<!DOCTYPE html>
<html lang="en">
<head>
<meta charset="utf-8">
<title>Tobias Wenger Rechtsanwalt</title>
<link rel="stylesheet" href="https://fonts.googleapis.com/css2?family=Montserrat:wght@400;500&family=Open+Sans:ital,wght@0,400;0,600;1,400&family=Poppins:wght@400;500&family=Roboto+Condensed:wght@400;700&display=swap">
<style>
:root{
  --blue:#0455a3;
  --blue-nav:#0b5cb6;
  --blue-dark:#033f7a;
  --ink:#333a44;
  --text:#555b63;
  --muted:#8a9098;
  --line:#e2e4e8;
  --page:#f5f5f5;
  --white:#ffffff;
  --footer:#1b1b1b;
  --red:#e0413a;
  --star:#f2a31b;
}
*{box-sizing:border-box;margin:0;padding:0}
html,body{width:1200px;height:2871px;overflow:hidden}
body{position:relative;background:var(--page);font-family:"Open Sans",sans-serif;color:var(--text)}
.abs{position:absolute}
a{color:inherit;text-decoration:none}

/* header */
.social-top{left:98px;top:51px;display:flex;gap:7px}
.social-top span{width:25px;height:25px;border-radius:50%;display:block}
.brand{left:0;width:1200px;top:46px;text-align:center;font-family:"Montserrat",sans-serif;font-size:24px;letter-spacing:2px;color:var(--blue-dark);font-weight:500}
.brand .light{color:#6b7480;font-weight:400}
.collab{left:963px;top:42px;width:138px;height:31px;background:var(--blue);color:var(--white);border-radius:3px;font-family:"Roboto Condensed",sans-serif;font-weight:700;font-size:13px;display:flex;align-items:center;justify-content:center;gap:6px}

/* nav */
.nav{left:98px;top:124px;width:1003px;height:54px;background:var(--blue-nav);font-family:"Roboto Condensed",sans-serif;font-size:15px;color:var(--white);text-transform:uppercase}
.nav a{position:absolute;top:18px}
.nav .search{position:absolute;left:954px;top:0;width:49px;height:54px;border-left:1px solid rgba(255,255,255,.2);display:flex;align-items:center;justify-content:center}
.dropdown{left:494px;top:178px;width:210px;z-index:3;background:rgba(11,92,182,.95);font-size:14px;color:var(--white)}
.dropdown li{list-style:none;height:43px;line-height:43px;padding-left:14px;border-bottom:1px solid rgba(255,255,255,.25)}
.dropdown li:last-child{border:0}

/* hero */
.hero{left:98px;top:178px;width:1003px;height:469px;background:linear-gradient(90deg,#6b5547 0%,#4a3a31 35%,#3a2c26 60%,#5a4034 100%);box-shadow:0 22px 28px -18px rgba(0,0,0,.45)}
.hero-title{left:712px;top:345px;font-family:"Roboto Condensed",sans-serif;font-weight:700;font-size:50px;line-height:54px;color:var(--white);text-transform:uppercase}
.hero-btn{left:712px;top:463px;width:109px;height:35px;background:var(--blue);color:var(--white);font-family:"Roboto Condensed",sans-serif;font-size:14px;display:flex;align-items:center;justify-content:center}
.dots{left:716px;top:527px;display:flex;gap:6px}
.dots span{width:13px;height:13px;border-radius:50%;border:2px solid var(--white)}
.dots span.on{background:var(--white)}

/* courses */
.section-title{left:0;width:1200px;top:692px;text-align:center;font-family:"Poppins",sans-serif;font-size:27px;color:var(--ink)}
.course{top:756px;width:324px;height:270px;background:var(--white);border:1px solid var(--line)}
.course .photo{height:220px}
.course p{text-align:center;font-family:"Poppins",sans-serif;font-size:18px;color:var(--ink);line-height:48px}

/* block headings */
.block-head{height:38px;border-bottom:2px solid var(--blue)}
.block-head span{display:inline-block;height:38px;line-height:38px;padding:0 60px 0 16px;background:var(--blue);color:var(--white);font-family:"Roboto Condensed",sans-serif;font-weight:700;font-size:21px;clip-path:polygon(0 0,84% 0,100% 100%,0 100%)}

/* articles */
.article{left:98px;width:698px;height:243px;background:var(--white);border:1px solid var(--line)}
.article .photo{position:absolute;left:0;top:0;width:306px;height:241px}
.article .body{position:absolute;left:332px;top:22px;width:345px}
.article h3{font-family:"Poppins",sans-serif;font-weight:400;font-size:16px;line-height:24px;color:var(--ink)}
.meta{display:flex;gap:26px;margin:18px 0 14px;font-size:12px;font-style:italic;color:var(--muted)}
.meta span{display:flex;gap:6px;align-items:center}
.article p{font-size:11.5px;line-height:22px;color:var(--text)}

/* feedback card */
.feedback{left:98px;top:1939px;width:698px;height:482px;background:var(--white);border:1px solid var(--line)}
.avatar{position:absolute;width:44px;height:44px;border-radius:50%;background:radial-gradient(circle at 50% 40%,#b08d74,#5b4438)}
.who{position:absolute;font-size:11px;color:var(--muted)}
.who b{display:block;font-weight:600;font-size:15px;color:#3f5fa6;margin-bottom:4px}
.rule{position:absolute;left:24px;width:648px;height:1px;background:var(--line)}
.post-title{position:absolute;left:201px;top:176px;font-family:"Poppins",sans-serif;font-size:16px;color:var(--ink)}
.post-text{position:absolute;left:201px;top:204px;width:455px;font-size:11px;line-height:19px}
.actions{position:absolute;left:24px;top:322px;display:flex;gap:22px;font-size:10.5px;color:var(--muted);text-transform:uppercase}
.actions span{display:flex;gap:6px;align-items:center;padding-right:22px;border-right:1px solid var(--line)}
.actions span:last-child{border:0}
.comment-box{position:absolute;left:74px;top:362px;width:571px;height:61px;border:1px solid #d6d8dc;border-radius:3px;font-size:11px;color:var(--ink);padding:10px 12px}
.post-btn{position:absolute;left:543px;top:438px;width:102px;height:23px;background:#ececec;border:1px solid #d0d2d6;font-size:11px;color:var(--text);display:flex;align-items:center;justify-content:center}

/* sidebar */
.search-box{left:836px;top:1072px;width:265px;height:44px;background:var(--white);border:1px solid #d3d6da;display:flex;align-items:center;justify-content:space-between;padding:0 14px 0 16px;font-size:11px;color:var(--muted)}
.book-promo{left:836px;top:1139px;width:265px;height:356px;background:#1f1a17}
.book-cover{position:absolute;left:56px;top:28px;width:150px;height:210px;background:linear-gradient(135deg,#7a2a25,#3d1614)}
.promo-input{position:absolute;left:37px;top:261px;width:190px;height:30px;background:var(--white);border-radius:3px;font-size:10px;color:var(--ink);display:flex;align-items:center;justify-content:center}
.promo-btn{position:absolute;left:37px;top:297px;width:190px;height:31px;background:var(--red);border-radius:3px;color:var(--white);font-family:"Roboto Condensed",sans-serif;font-size:15px;display:flex;align-items:center;justify-content:center}
.recent{left:836px;top:1564px;width:265px;height:497px;background:var(--white);border:1px solid var(--line);border-top:0}
.recent-item{position:absolute;left:19px;width:230px;height:110px}
.recent-item .thumb{position:absolute;left:0;top:0;width:98px;height:108px;background:linear-gradient(160deg,#c9c3bb,#4b4f57)}
.recent-item .txt{position:absolute;left:114px;top:0;width:116px}
.recent-item h4{font-family:"Poppins",sans-serif;font-weight:400;font-size:14px;color:var(--ink)}
.stars{color:var(--star);font-size:11px;letter-spacing:1px;margin:6px 0 4px}
.stars i{color:#cfd2d6;font-style:normal}
.recent-item p{font-size:10.5px;line-height:17px}
.count{font-size:10px;font-style:italic;color:var(--muted);margin-top:6px;display:flex;gap:6px;align-items:center}
.video{left:836px;top:2155px;width:265px;height:171px;background:linear-gradient(180deg,#9b7b62 0%,#6e5544 60%,#4a3a2f 100%)}
.video-text{left:836px;top:2345px;width:265px;font-size:11px;line-height:20px}
.video-count{left:836px;top:2396px;font-size:10px;font-style:italic;color:var(--muted);display:flex;gap:6px;align-items:center}

/* footer */
.footer{left:0;top:2507px;width:1200px;height:364px;background:var(--footer);color:var(--white)}
.footer h5{position:absolute;top:47px;font-family:"Roboto Condensed",sans-serif;font-weight:700;font-size:16px;text-transform:uppercase}
.footer .signup-text{position:absolute;left:98px;top:90px;width:300px;font-size:11px;line-height:20px}
.footer .name-field{position:absolute;left:98px;top:138px;width:286px;height:40px;background:var(--white);color:#666;font-size:11px;padding:0 14px;display:flex;align-items:center}
.footer .sub-btn{position:absolute;left:98px;top:192px;width:100px;height:40px;background:var(--blue);font-family:"Roboto Condensed",sans-serif;font-size:13px;display:flex;align-items:center;justify-content:center}
.footer ul{position:absolute;list-style:none;font-size:11.5px;line-height:24px}
.contact-row{position:absolute;left:706px;display:flex;gap:14px;font-size:11.5px;line-height:20px}
.social-row{position:absolute;left:1001px;display:flex;gap:12px;align-items:center;font-size:13px}
.social-row span{width:28px;height:28px;border:1.5px solid var(--white);border-radius:50%}
.copyright{position:absolute;left:0;width:1200px;top:2835px;text-align:center;font-size:11.5px;color:var(--white)}
</style>
</head>
<body>

<header>
  <div class="abs social-top" aria-label="Social links">
    <span style="background:#3b5ea8"></span>
    <span style="background:#f2a33a"></span>
    <span style="background:#3ea6e0"></span>
    <span style="background:#4fc2d6"></span>
    <span style="background:#e0413a"></span>
  </div>
  <div class="abs brand">TOBIAS WENGER <span class="light">RECHTSANWALT</span></div>
  <a class="abs collab" href="#">
    <svg width="10" height="12" viewBox="0 0 10 12"><rect x="1" y="5" width="8" height="7" rx="1" fill="#fff"/><path d="M3 5V3.5a2 2 0 0 1 4 0V5" stroke="#fff" stroke-width="1.4" fill="none"/></svg>
    COLLABORATE
  </a>
</header>

<nav class="abs nav">
  <a href="#" style="left:30px">Home</a>
  <a href="#" style="left:130px">Articles</a>
  <a href="#" style="left:252px">Law &amp; Politics</a>
  <a href="#" style="left:421px">University Courses</a>
  <a href="#" style="left:631px">Projects</a>
  <a href="#" style="left:761px">Contact Us</a>
  <span class="search"><svg width="14" height="14" viewBox="0 0 14 14"><circle cx="6" cy="6" r="4.5" stroke="#fff" stroke-width="1.6" fill="none"/><path d="M9.3 9.3L13 13" stroke="#fff" stroke-width="1.6"/></svg></span>
</nav>

<section class="abs hero" role="img" aria-label="Portrait of a smiling man in a dark suit and red tie in front of shelves of law books"></section>
<ul class="abs dropdown">
  <li>Constitutional</li>
  <li>Administrative</li>
  <li>International Law</li>
</ul>
<h1 class="abs hero-title">Tobias Wenger<br>Rechtsanwalt</h1>
<a class="abs hero-btn" href="#">READ MORE</a>
<div class="abs dots"><span class="on"></span><span></span><span></span></div>

<h2 class="abs section-title">My University Courses</h2>
<article class="abs course" style="left:98px">
  <div class="photo" role="img" aria-label="Three colleagues discussing documents at a table" style="background:linear-gradient(135deg,#d9d4cc,#8a8c91)"></div>
  <p>Constitutional</p>
</article>
<article class="abs course" style="left:438px">
  <div class="photo" role="img" aria-label="Man in a suit working at a laptop in an office" style="background:linear-gradient(135deg,#8a6a4d,#4a4b52)"></div>
  <p>Administrative</p>
</article>
<article class="abs course" style="left:777px">
  <div class="photo" role="img" aria-label="Lawyer with folded arms in front of a library of law books" style="background:linear-gradient(135deg,#a0683c,#5a4032)"></div>
  <p>International Law</p>
</article>

<div class="abs block-head" style="left:98px;top:1076px;width:698px"><span>LATEST ARTICLES</span></div>

<article class="abs article" style="top:1135px">
  <div class="photo" role="img" aria-label="Businessmen in dark suits buttoning their jackets" style="background:linear-gradient(135deg,#cfcac3,#3a3c42)"></div>
  <div class="body">
    <h3>How to win in Court , Nemo enim ipsam voluptatem quia</h3>
    <div class="meta"><span>&#9638; Jan 25, 2017</span><span>&#9711; 2 comments</span><span>&#9998; by David</span></div>
    <p>Whereas court proceedings tend to be complicated, judges are not. In fact, they are rather simple creatures. This is why they like it simple. And this is why it is not always that hard to win in court. All you have to do is reduce the complexity of the case.</p>
  </div>
</article>
<article class="abs article" style="top:1401px">
  <div class="photo" role="img" aria-label="Businessman reading a tablet in a brick-walled office" style="background:linear-gradient(135deg,#9a5a3c,#3f4856)"></div>
  <div class="body">
    <h3>How to win in Court , Nemo enim ipsam voluptatem quia</h3>
    <div class="meta"><span>&#9638; Jan 25, 2017</span><span>&#9711; 2 comments</span><span>&#9998; by David</span></div>
    <p>Whereas court proceedings tend to be complicated, judges are not. In fact, they are rather simple creatures. This is why they like it simple. And this is why it is not always that hard to win in court. All you have to do is reduce the complexity of the case.</p>
  </div>
</article>
<article class="abs article" style="top:1667px">
  <div class="photo" role="img" aria-label="Group of colleagues reviewing a blue folder together" style="background:linear-gradient(135deg,#8c8a5a,#3b3f4a)"></div>
  <div class="body">
    <h3>How to win in Court , Nemo enim ipsam voluptatem quia</h3>
    <div class="meta"><span>&#9638; Jan 25, 2017</span><span>&#9711; 2 comments</span><span>&#9998; by David</span></div>
    <p>Whereas court proceedings tend to be complicated, judges are not. In fact, they are rather simple creatures. This is why they like it simple. And this is why it is not always that hard to win in court. All you have to do is reduce the complexity of the case.</p>
  </div>
</article>

<section class="abs feedback">
  <div class="avatar" style="left:24px;top:22px" role="img" aria-label="Profile photo"></div>
  <div class="who" style="left:78px;top:28px"><b>Jonas Frei</b>sed do eiusmod tempor incididunt</div>
  <div class="rule" style="top:74px"></div>
  <div class="avatar" style="left:24px;top:90px" role="img" aria-label="Profile photo"></div>
  <div class="who" style="left:78px;top:96px"><b>Jonas Frei</b>319 Reviews , 432 Followers</div>
  <div role="img" aria-label="Man standing in a library" style="position:absolute;left:23px;top:170px;width:153px;height:92px;background:linear-gradient(135deg,#a0683c,#4b3a30)"></div>
  <div class="post-title">Sed ut perspiciatis unde omnis iste natus</div>
  <p class="post-text">sed do eiusmod tempor incididunt ut labore et dolore magna aliqua. Ut enim ad minim veniam, quis nostrud exercitation ullamco laboris nisi ut aliquip ex ea commodo consequat. Duis aute irure</p>
  <div class="rule" style="top:304px"></div>
  <div class="actions"><span>&#128077;&#xFE0E; Like</span><span>&#9641; Comment</span><span>&#10150; Share</span></div>
  <div class="avatar" style="left:24px;top:358px" role="img" aria-label="Profile photo"></div>
  <div class="comment-box">write a comment</div>
  <div class="post-btn">Post Comment</div>
</section>

<aside>
  <div class="abs search-box">SEARCH <svg width="12" height="12" viewBox="0 0 14 14"><circle cx="6" cy="6" r="4.5" stroke="#333" stroke-width="1.8" fill="none"/><path d="M9.3 9.3L13 13" stroke="#333" stroke-width="1.8"/></svg></div>
  <div class="abs book-promo">
    <div class="book-cover" role="img" aria-label="Book cover: Statutes and Society - Notes from the Chamber"></div>
    <div class="promo-input">Enter Your E - Mail</div>
    <div class="promo-btn">SUBSCRIBE</div>
  </div>

  <div class="abs block-head" style="left:836px;top:1525px;width:265px"><span style="padding-right:48px">RECENT POSTS</span></div>
  <div class="abs recent">
    <div class="recent-item" style="top:34px">
      <div class="thumb" role="img" aria-label="Portrait of a man in a suit"></div>
      <div class="txt"><h4>Duis aute irure</h4><div class="stars">★★★<i>★★</i></div><p>Lorem ipsum dolor sit amet, consectetur</p><div class="count">&#9711; 2 comments</div></div>
    </div>
    <div class="recent-item" style="top:197px">
      <div class="thumb" role="img" aria-label="Portrait of a man in a suit"></div>
      <div class="txt"><h4>Duis aute irure</h4><div class="stars">★★★<i>★★</i></div><p>Lorem ipsum dolor sit amet, consectetur</p><div class="count">&#9711; 2 comments</div></div>
    </div>
    <div class="recent-item" style="top:360px">
      <div class="thumb" role="img" aria-label="Portrait of a man in a suit"></div>
      <div class="txt"><h4>Duis aute irure</h4><div class="stars">★★★<i>★★</i></div><p>Lorem ipsum dolor sit amet, consectetur</p><div class="count">&#9711; 2 comments</div></div>
    </div>
  </div>

  <div class="abs block-head" style="left:836px;top:2092px;width:265px"><span style="padding-right:48px">VIDEO BLOG</span></div>
  <div class="abs video" role="img" aria-label="Video still of a woman standing in a corridor">
    <svg width="58" height="58" viewBox="0 0 58 58" style="position:absolute;left:104px;top:56px"><circle cx="29" cy="29" r="27" fill="rgba(0,0,0,.25)" stroke="#fff" stroke-width="2"/><path d="M23 18L41 29L23 40Z" fill="#fff"/></svg>
  </div>
  <p class="abs video-text">Lorem ipsum dolor sit amet, consectetur adipiscing elit, sed do eiusmod tempor incididunt</p>
  <div class="abs video-count">&#9711; 2 comments</div>
</aside>

<footer class="abs footer">
  <h5 style="left:98px">Sign up to receive email</h5>
  <p class="signup-text">Excepteur sint occaecat cupidatat non proident, sunt in culpa qui Nemo enim ipsam voluptatem</p>
  <div class="name-field">Enter Name</div>
  <div class="sub-btn">SUBSCRIBE</div>

  <h5 style="left:505px">Quick Links</h5>
  <ul style="left:505px;top:88px">
    <li>Home</li><li>Articles</li><li>Law &amp; Politics</li><li>University Courses</li><li>Projects</li><li>Contact us</li>
  </ul>

  <h5 style="left:706px">Contact Us</h5>
  <div class="contact-row" style="top:90px">
    <svg width="12" height="16" viewBox="0 0 12 16"><path d="M6 0a6 6 0 0 0-6 6c0 4.5 6 10 6 10s6-5.5 6-10a6 6 0 0 0-6-6z" fill="#fff"/><circle cx="6" cy="6" r="2.2" fill="#1b1b1b"/></svg>
    <span>Tobias Wenger Rechtsanwalt<br>Seefeld ZH 8008</span>
  </div>
  <div class="contact-row" style="top:143px">
    <svg width="14" height="14" viewBox="0 0 14 14"><path d="M3 0l3 3-2 2c1 2 3 4 5 5l2-2 3 3-2 3C6 14 0 8 0 3z" fill="#fff"/></svg>
    <span>Phone: (044) 555-0147</span>
  </div>
  <div class="contact-row" style="top:183px">
    <svg width="14" height="11" viewBox="0 0 14 11"><rect width="14" height="11" rx="1" fill="#fff"/><path d="M0 1l7 5 7-5" stroke="#1b1b1b" stroke-width="1.3" fill="none"/></svg>
    <span>info@civicnorm.example</span>
  </div>

  <h5 style="left:1001px">Social Media</h5>
  <div class="social-row" style="top:86px"><span></span>Townhall</div>
  <div class="social-row" style="top:124px"><span></span>Chirpline</div>
  <div class="social-row" style="top:162px"><span></span>Orbitnet</div>
  <div class="social-row" style="top:200px"><span></span>Reelcast</div>
</footer>
<p class="copyright">Copyright © Tobias Wenger Rechtsanwalt 2017. All rights reserved.</p>

</body>
</html>
```